Webdesign für Frauen-Personal-Training
Sehr schnelle Umsetzung meiner Wünsche und Ideen
Zielgruppe
Personal Training für Frauen in Führungspositionen ab 30 Jahren
Aufgabenstellung
Bilderwelt stimmig, Farbfokus auf CI Farben (im Anhang wie auch Logo), 1/3 Text, 2/3 Bilderwelt
- Hamburger Menü, kein klassisches
- Footer: Anschrift, Datenschutz, Impressum
- Headerimage mit Seitentitel im Bild, Titelunterschrift 2/3 der Bildschirmhöhe
- Berücksichtigung von Whitespace
- Verwendung von Icons zum Beispiel auf der Startseite beim Punkt 'du suchst - ich biete'
Seiten:
- Startseite: Einstieg für Besucher der Homepage in der Richtung 'du suchst, ich biete', abschließend Formular --> Abschluss Kontaktformular
- Training: Trainingsweise und Arbeitsweise beschreiben
- Über mich (Aufbau der Seite gleich wie 'Training' und 'Preise'): Professionelle Erfahrungen in Richtung training, Ernährung, Gesundheit --> Abschluss: CTA 'Nimm Kontakt zu mir auf und informiere dich in einem persönlichen Gespräch --> Link auf Kontaktseite
- Räumlichkeiten --> Abschluss: CTA 'Nimm Kontakt zu mir auf und informiere dich in einem persönlichen Gespräch --> Link auf Kontaktseite
- Preise --> Abschluss: CTA 'Nimm Kontakt zu mir auf und informiere dich in einem persönlichen Gespräch --> Link auf Kontaktseite
- Kontaktseite (Landing Page)
(- Impressum / Datenschutzseite)
Beispielseite:
https://www.quintello.com/rastavoni

```html
<!DOCTYPE html>
<html lang="de">
<head>
<meta charset="utf-8">
<title>Formwerk – Personal Training für Frauen</title>
<link href="https://fonts.googleapis.com/css2?family=Titillium+Web:wght@300;400;600&family=Rubik:wght@300;400;500&display=swap" rel="stylesheet">
<style>
:root{
  --olive:#7b735b;
  --green:#679d7b;
  --ink:#1f1f1f;
  --text:#555;
  --band:#f6f6f6;
  --panel:#efefef;
  --footer:#1c1c1c;
  --white:#fff;
}
*{margin:0;padding:0;box-sizing:border-box}
html,body{width:1200px;height:4521px;overflow:hidden}
body{position:relative;background:var(--white);font-family:'Rubik',sans-serif;color:var(--ink)}
.abs{position:absolute}
.head{font-family:'Titillium Web',sans-serif;font-weight:400;color:var(--ink);line-height:1.05}
.kicker{font-family:'Rubik',sans-serif;font-size:14px;color:var(--green);text-transform:uppercase;letter-spacing:.3px}
.copy{font-size:11.5px;line-height:22.5px;color:var(--text)}
.btn{background:var(--green);color:var(--white);font-size:12px;font-weight:500;letter-spacing:1.6px;display:flex;align-items:center;justify-content:center;text-transform:uppercase}
.photo{background:linear-gradient(135deg,#c9cfd4,#8a96a3 60%,#5b6a7a)}
/* header */
.hero-band{left:484px;top:0;width:716px;height:649px;background:var(--olive)}
.logo{left:93px;top:14px;display:flex;align-items:center;gap:8px;font-size:20px;font-weight:500;color:var(--green)}
.logo span.dot{width:10px;height:10px;border-radius:50%;background:var(--green)}
.logo small{display:block;font-size:9px;color:var(--green);font-weight:400;margin-top:-2px}
.burger{left:1076px;top:27px;width:28px}
.burger i{display:block;height:2px;background:var(--white);margin-bottom:6px}
.hero-img{left:93px;top:61px;width:1012px;height:532px;background:linear-gradient(100deg,#dfe3e2 0%,#b9c3c8 45%,#7f93a6 75%,#4d6075 100%)}
.hero-title{left:231px;top:268px;font-size:39px}
.slider{left:233px;top:614px;width:180px;height:14px}
/* benefits */
.band{left:0;top:1002px;width:600px;height:805px;background:var(--band)}
.col-title{font-family:'Titillium Web',sans-serif;font-size:21px;color:var(--green)}
.item h3{font-family:'Rubik',sans-serif;font-weight:400;font-size:16px;color:var(--ink);margin-bottom:10px}
.item p{font-size:10.5px;line-height:22.5px;color:var(--text);width:250px}
.ring{width:134px;height:134px}
/* story */
.quote{background:var(--green);color:var(--white);font-size:18.5px;line-height:30px;padding:28px 26px}
.label{background:var(--white);font-family:'Titillium Web',sans-serif;font-size:18px;line-height:21px;color:var(--ink)}
.arrow{height:8px}
/* contact */
.footer{left:0;top:4455px;width:1200px;height:66px;background:var(--footer);color:var(--white);font-size:9px;letter-spacing:1px}
</style>
</head>
<body>

<!-- header / hero -->
<div class="abs hero-band"></div>
<div class="abs logo"><span class="dot"></span><div>Formwerk<small>Personal Training für Frauen</small></div></div>
<div class="abs burger" aria-label="Menü"><i></i><i></i></div>
<div class="abs hero-img" role="img" aria-label="Foto: lächelnde Geschäftsfrau vor Bürogebäuden"></div>
<div class="abs kicker" style="left:233px;top:240px">Unsere Strategie</div>
<h1 class="abs head hero-title">90% der Frauen in<br>Führungspositionen<br>bewegen sich zu wenig</h1>
<div class="abs btn" style="left:233px;top:418px;width:169px;height:38px">Mehr Info</div>
<svg class="abs slider" viewBox="0 0 180 14">
  <line x1="2" y1="7" x2="48" y2="7" stroke="#bbb" stroke-width="1"/>
  <path d="M6 4 L2 7 L6 10" fill="none" stroke="#bbb"/>
  <circle cx="68" cy="7" r="3" fill="none" stroke="#333"/><circle cx="68" cy="7" r="1.3" fill="#333"/>
  <circle cx="88" cy="7" r="1.6" fill="#999"/><circle cx="107" cy="7" r="1.6" fill="#999"/>
  <line x1="127" y1="7" x2="174" y2="7" stroke="#333"/>
  <path d="M170 4 L174 7 L170 10" fill="none" stroke="#333"/>
</svg>

<!-- Beratungsleistungen -->
<div class="abs kicker" style="left:233px;top:770px">Beratungsleistungen</div>
<h2 class="abs head" style="left:231px;top:795px;font-size:38px">Person Vorteile</h2>
<p class="abs copy" style="left:233px;top:874px;width:545px">Lorem ipsum dolor sit amet, consectetur adipiscing elit. Curabitur fermentum placerat augue ut volut-pat. Pellentesque ultrices finibus justo, non cursus ante lacinia sit amet. Donec porttitor ex odio, nec po-suere nibh convallis vel. Duis tempor orci sit amet aliquet blandit. Integer congue odio id felis ornare, non tempus velit sagittis. Proin ac enim neque. Morbi non sagittis leo, ut tincidunt enim. Phasellus non dolor sit amet orci dignissim mollis. Morbi ut dapibus ligula. Sed eget sagittis justo.</p>

<div class="abs band"></div>
<div class="abs col-title" style="left:233px;top:1024px">Sie suchen</div>
<div class="abs col-title" style="left:694px;top:1024px">Ich biete</div>

<div class="abs item" style="left:233px;top:1100px"><h3>Kompetenz</h3><p>Jemanden, der auf Ihre Anliegen, Wünsche und Fragen die richtigen Antworten kennt</p></div>
<div class="abs item" style="left:694px;top:1100px"><h3>Kompetenz</h3><p>Zahlreiche Aus- und Fortbildungen, langjährige Praxis und der Anspruch, jeden Tag besser zu werden</p></div>
<div class="abs item" style="left:233px;top:1260px"><h3>Individualität</h3><p>Jemanden, der ein auf Sie und Ihre Wünsche zugeschneidertes Konzept erarbeitet und durchführt</p></div>
<div class="abs item" style="left:694px;top:1260px"><h3>Individualität</h3><p>"es kommt darauf an", nach diesem Motto schauen wir gemeinsam, was für Sie passt und was nicht</p></div>
<div class="abs item" style="left:233px;top:1421px"><h3>Aufmerksamkeit</h3><p>Jemanden, der sich voll und ganz auf Sie konzentriert</p></div>
<div class="abs item" style="left:694px;top:1421px"><h3>Aufmerksamkeit</h3><p>Im Training stehst du im Mittelpunkt</p></div>
<div class="abs item" style="left:233px;top:1582px"><h3>Diskretion</h3><p>Einen Ort, an dem Sie ohne Bedenken Sie selbst sein können</p></div>
<div class="abs item" style="left:694px;top:1582px"><h3>Diskretion</h3><p>Meine Akzeptanz in Kombination mit eigenen Räumlichkeiten</p></div>

<svg class="abs ring" style="left:533px;top:1064px" viewBox="0 0 134 134">
  <circle cx="67" cy="67" r="66" fill="#fff" stroke="#ececec"/><circle cx="67" cy="67" r="36" fill="none" stroke="#e2e2e2" stroke-width="6"/>
  <path d="M67 31 A36 36 0 0 1 67 103" fill="none" stroke="var(--green)" stroke-width="6"/>
  <g fill="none" stroke="#777" stroke-width="1.5"><circle cx="66" cy="67" r="13"/><circle cx="66" cy="67" r="8"/><circle cx="66" cy="67" r="3"/><path d="M66 67 L80 60 M77 58 L82 59 L80 63"/></g>
</svg>
<svg class="abs ring" style="left:533px;top:1227px" viewBox="0 0 134 134">
  <circle cx="67" cy="67" r="66" fill="#fff" stroke="#ececec"/><circle cx="67" cy="67" r="36" fill="none" stroke="#e2e2e2" stroke-width="6"/>
  <path d="M67 31 A36 36 0 0 1 67 103" fill="none" stroke="var(--green)" stroke-width="6"/>
  <g fill="none" stroke="#777" stroke-width="1.5"><circle cx="67" cy="67" r="14"/><path d="M67 58 L69.6 64 L76 64.4 L71 68.5 L72.6 75 L67 71.5 L61.4 75 L63 68.5 L58 64.4 L64.4 64 Z"/></g>
</svg>
<svg class="abs ring" style="left:533px;top:1387px" viewBox="0 0 134 134">
  <circle cx="67" cy="67" r="66" fill="#fff" stroke="#ececec"/><circle cx="67" cy="67" r="36" fill="none" stroke="#e2e2e2" stroke-width="6"/>
  <path d="M67 31 A36 36 0 0 1 67 103" fill="none" stroke="var(--green)" stroke-width="6"/>
  <g fill="none" stroke="#777" stroke-width="1.5"><path d="M67 52 L84 80 L50 80 Z"/><path d="M67 56 L80 77 L54 77 Z"/><path d="M67 63 L67 71 M67 74 L67 75"/></g>
</svg>
<svg class="abs ring" style="left:533px;top:1547px" viewBox="0 0 134 134">
  <circle cx="67" cy="67" r="66" fill="#fff" stroke="#ececec"/><circle cx="67" cy="67" r="36" fill="none" stroke="#e2e2e2" stroke-width="6"/>
  <path d="M67 31 A36 36 0 0 1 67 103" fill="none" stroke="var(--green)" stroke-width="6"/>
  <g fill="none" stroke="#777" stroke-width="1.5"><rect x="56" y="64" width="22" height="18" rx="2"/><path d="M60 64 V58 A7 7 0 0 1 74 58 V64"/><path d="M67 70 V76"/></g>
</svg>
<div class="abs btn" style="left:507px;top:1733px;width:186px;height:39px">Kontakt zu mir</div>

<!-- Über mich -->
<div class="abs kicker" style="left:233px;top:1931px">Über mich</div>
<h2 class="abs head" style="left:231px;top:1955px;font-size:40px">Meine persönliche<br>Geschichte</h2>
<p class="abs copy" style="left:421px;top:2076px;width:548px">Suspendisse ut auctor massa. Nunc a semper odio. Pellentesque volutpat dolor sit amet gravida suscipit. Integer ultricies neque diam, sit amet rhoncus dui vehicula sit amet. Etiam a vestibulum turpis. Proin purus quam, egestas a massa convallis, pellentesque volutpat risus. Proin maximus ornare eros viverra viverra. Interdum et malesuada fames ac ante ipsum primis in faucibus. Vestibulum tristique neque sit amet lectus mattis, ut placerat eros porta. Proin purus quam, egestas a massa convallis, pellentesque volutpat risus.</p>
<div class="abs photo" style="left:419px;top:2259px;width:546px;height:312px;background:linear-gradient(100deg,#2f3a55 0%,#5b6478 35%,#e4e6e8 55%,#9aa6b5 80%,#3a4c68 100%)" role="img" aria-label="Foto: Händedruck zwischen Geschäftsleuten"></div>
<div class="abs quote" style="left:233px;top:2408px;width:295px;height:213px">Mit unseren Spezialisten und Experten, die Ihnen zur Verfügung stehen, werden Sie komplexe Probleme mit Zuversicht angehen</div>

<!-- Kurse -->
<div class="abs" style="left:233px;top:2740px;width:62px;height:3px;background:var(--green)"></div>
<h2 class="abs head" style="left:231px;top:2758px;font-size:40px">Unsere Kurse</h2>
<div class="abs" style="left:281px;top:3043px;width:310px;height:109px;background:var(--olive)"></div>
<div class="abs photo" style="left:233px;top:2841px;width:358px;height:255px;background:linear-gradient(120deg,#4a5f8a,#c8c0b5 50%,#d8c56a 80%,#e9e6df)" role="img" aria-label="Foto: gestapelte Hände im Team"></div>
<div class="abs label" style="left:298px;top:3040px;width:293px;height:96px;padding:17px 0 0 19px">Teambuilding und<br>Teammanagement<br>Online Kurse</div>
<svg class="abs arrow" style="left:541px;top:3090px;width:46px" viewBox="0 0 46 8"><line x1="0" y1="4" x2="44" y2="4" stroke="#aaa"/><path d="M40 1 L44 4 L40 7" fill="none" stroke="#aaa"/></svg>

<div class="abs photo" style="left:609px;top:2941px;width:356px;height:258px;background:linear-gradient(120deg,#e8ebee,#b9c2cc 50%,#6d7f93 75%,#dcdfe2)" role="img" aria-label="Foto: Geschäftsbesprechung mit Diagrammen und Tablet"></div>
<div class="abs label" style="left:670px;top:3140px;width:295px;height:72px;padding:18px 0 0 23px">Betriebsführung und<br>strategische Planung</div>
<svg class="abs arrow" style="left:915px;top:3183px;width:46px" viewBox="0 0 46 8"><line x1="0" y1="4" x2="44" y2="4" stroke="#aaa"/><path d="M40 1 L44 4 L40 7" fill="none" stroke="#aaa"/></svg>

<p class="abs copy" style="left:421px;top:3262px;width:548px">Nam a pharetra lacus. Maecenas a sapien interdum felis vehicula egestas. Sed dapibus sapien sed eros pretium dignissim. Curabitur consequat dui vel pellentesque commodo. Proin quis turpis finibus, congue nibh sit amet, molestie tellus. Orci varius natoque penatibus et magnis dis parturient montes, nascetur ridiculus mus. Nam nibh diam, mattis et pellentesque eget, commodo at tortor.</p>
<div class="abs btn" style="left:423px;top:3394px;width:168px;height:40px">Mehr Info</div>

<!-- Gründerin -->
<div class="abs photo" style="left:233px;top:3559px;width:483px;height:338px;background:linear-gradient(90deg,#e9ecee,#cfd5da 45%,#2f3d5e 60%,#e3e6e8 85%)" role="img" aria-label="Portraitfoto der Gründerin im Büro"></div>
<div class="abs copy" style="left:733px;top:3603px;font-size:10.5px">Mara Keller<br>Gründer</div>
<div class="abs copy" style="left:733px;top:3669px;font-size:10.5px">Berlin 2019</div>
<div class="abs" style="left:951px;top:3675px;width:10px;height:10px;background:var(--ink)" aria-label="Profil"></div>
<div class="abs quote" style="left:672px;top:3736px;width:293px;height:211px;padding:30px 26px">Nimm Kontakt zu mir auf und informiere dich in einem persönlichen Gespräch</div>
<svg class="abs arrow" style="left:887px;top:3902px;width:48px" viewBox="0 0 48 8"><line x1="0" y1="4" x2="46" y2="4" stroke="#fff"/><path d="M42 1 L46 4 L42 7" fill="none" stroke="#fff"/></svg>

<!-- Kontaktformular -->
<div class="abs" style="left:0;top:4069px;width:840px;height:386px;background:var(--olive)"></div>
<div class="abs" style="left:93px;top:4134px;width:1012px;height:321px;background:var(--panel)"></div>
<div class="abs" style="left:596px;top:4196px;width:32px;height:3px;background:var(--green)"></div>
<h2 class="abs head" style="left:0;top:4212px;width:1200px;text-align:center;font-size:40px">Kontaktformular</h2>
<p class="abs" style="left:0;top:4268px;width:1200px;text-align:center;font-size:17px;color:var(--ink)">Professionelle Erfahrungen in Richtung training, Ernährung, Gesundheit</p>
<div class="abs" style="left:421px;top:4318px;font-size:9.5px;letter-spacing:1px;font-weight:500">E-MAIL:</div>
<div class="abs" style="left:421px;top:4336px;width:356px;height:37px;background:var(--white)"></div>
<svg class="abs arrow" style="left:711px;top:4351px;width:48px" viewBox="0 0 48 8"><line x1="0" y1="4" x2="46" y2="4" stroke="#333"/><path d="M42 1 L46 4 L42 7" fill="none" stroke="#333"/></svg>
<div class="abs" style="left:421px;top:4379px;width:356px;height:3px;background:#ddd"></div>
<div class="abs" style="left:421px;top:4379px;width:88px;height:3px;background:var(--green)"></div>
<div class="abs" style="left:760px;top:4387px;font-size:9px;font-weight:500">2/6</div>

<!-- Footer -->
<footer class="abs footer">
  <span class="abs" style="left:233px;top:28px;font-weight:500">IMPRESSUM</span>
  <span class="abs" style="left:321px;top:28px;font-weight:500">DATENSCHUTZSEITE</span>
  <span class="abs" style="left:868px;top:28px;letter-spacing:0">© Formwerk 2019</span>
</footer>

</body>
</html>
```